Email Signature Design

Please design an email signature, the below is an example of our current design;
___

CORMACK ESTATE HOLDINGS PTY LTD
BARNABY CORMACK
Licensed Strata and Community Manager

164 Tallowood Street,
ULTIMO NSW 2007

P: 02.9376.5820 F: 9463.7208
Website: www.cormackestates.com.au

This e-mail message and accompanying data may contain information that is confidential and private. If you are not the intended recipient, the use, dissemination, distribution or copying of this message or data is prohibited.

If you have received this e-mail in error please notify us immediately and delete all material pertaining to this e-mail. strata@cormackestates.com.au

___

We would like to incorporate our logo and company colours, you can view the colours and feel of image at www.cormackestates.com.au

Industry/Entity Type

It Company

Requirements
Must have
• use of logo and company colours (image)

```html
<!DOCTYPE html>
<html lang="en">
<head>
<meta charset="utf-8">
<title>Cormack Estate Holdings – Email Signatures</title>
<link href="https://fonts.googleapis.com/css2?family=Arimo:wght@400;700&display=swap" rel="stylesheet">
<style>
  :root {
    --olive: #857f2e;
    --text-grey: #5e5e5e;
    --notice-grey: #555555;
    --rule: #c9c59a;
    --social: #6a6a6a;
    --card: #ffffff;
    --backdrop: #2b2b2b;
    --watermark: #f2f2ec;
  }
  * { margin: 0; padding: 0; box-sizing: border-box; }
  html, body { width: 1200px; height: 900px; overflow: hidden; }
  body {
    background: var(--backdrop);
    font-family: "Arimo", Arial, sans-serif;
    color: var(--text-grey);
    position: relative;
  }
  .signature {
    position: absolute;
    left: 205px;
    width: 790px;
    height: 262px;
    background: var(--card);
    overflow: hidden;
  }
  .signature > * { position: absolute; white-space: nowrap; }
  .brand-backdrop { background: var(--watermark); width: 180px; height: 180px; top: 0; left: 600px; }
  .brand-mark { background: var(--olive); }
  .person-name { font-size: 15.5px; font-weight: 700; color: var(--olive); }
  .person-role { font-size: 11px; }
  .contact { font-size: 11.5px; display: flex; align-items: center; gap: 4px; }
  .contact svg { width: 11px; height: 11px; fill: var(--olive); flex: none; }
  .contact .gap { width: 6px; }
  .company { font-size: 10.5px; font-weight: 700; color: var(--olive); }
  .address { font-size: 11.5px; line-height: 16px; }
  .brand-name { font-weight: 700; color: var(--olive); letter-spacing: 0.2px; }
  .brand-tag { color: var(--text-grey); letter-spacing: 0.6px; }
  .divider { width: 1px; background: var(--rule); }
  .notice { font-size: 8px; line-height: 11px; color: var(--notice-grey); white-space: normal; }
  .social { display: flex; gap: 5px; }
  .social span { width: 12px; height: 12px; background: var(--social); border-radius: 1px; display: block; }
</style>
</head>
<body>

<svg width="0" height="0" style="position:absolute" aria-hidden="true">
  <symbol id="icon-phone" viewBox="0 0 12 12"><path d="M3 1 L5 3.5 L4 5 Q5 7 7 8 L8.5 7 L11 9 L9.5 11 Q5 11 2.5 7.5 Q1 5 1.2 2.5 Z" fill="none" stroke="currentColor" stroke-width="1"/></symbol>
  <symbol id="icon-fax" viewBox="0 0 12 12"><rect x="3" y="1" width="6" height="3"/><rect x="1" y="4.5" width="10" height="4.5" rx="1"/><rect x="3" y="9.5" width="6" height="1.8"/></symbol>
  <symbol id="icon-web" viewBox="0 0 12 12"><circle cx="6" cy="6" r="5" fill="none" stroke="currentColor" stroke-width="1"/><ellipse cx="6" cy="6" rx="2.2" ry="5" fill="none" stroke="currentColor" stroke-width="1"/><path d="M1 6 H11 M2 3.5 H10 M2 8.5 H10" stroke="currentColor" stroke-width="0.8"/></symbol>
</svg>

<!-- Layout one: contact left, brand centred -->
<section class="signature" style="top:50px">
  <div class="brand-backdrop"></div>
  <div class="brand-mark" style="left:345px;top:34px;width:96px;height:96px"></div>
  <div class="person-name" style="left:36px;top:52px">BARNABY CORMACK</div>
  <div class="person-role" style="left:36px;top:71px">Licensed Strata and Community Manager</div>
  <div class="contact" style="left:36px;top:110px">
    <svg style="color:var(--olive)"><use href="#icon-phone"/></svg>02.9376.5820<span class="gap"></span>
    <svg><use href="#icon-fax"/></svg>9463.7208
  </div>
  <div class="contact" style="left:36px;top:126px">
    <svg style="color:var(--olive)"><use href="#icon-web"/></svg>www.cormackestates.com.au
  </div>
  <div class="company" style="left:36px;top:154px">CORMACK ESTATE HOLDINGS PTY LTD</div>
  <div class="address" style="left:36px;top:167px">164 Tallowood Street, ULTIMO NSW 2007</div>
  <div class="brand-name" style="left:316px;top:143px;font-size:19px">CORMACK ESTATE GROUP</div>
  <div class="brand-tag" style="left:317px;top:166px;font-size:13.5px">STRATA MANAGEMENT SERVICES</div>
  <div class="social" style="left:705px;top:168px"><span></span><span></span><span></span><span></span></div>
  <p class="notice" style="left:36px;top:212px;width:730px">NOTICE: This e-mail message and accompanying data may contain information that is confidential and private If you are not the intended recipient, the use, dissemination, distribution or copying of this message or data is prohibited.</p>
  <p class="notice" style="left:36px;top:244px;width:730px">If you have received this e-mail in error please notify us immediately and delete all material pertaining to this e-mail. strata@cormackestates.com.au</p>
</section>

<!-- Layout two: single-line contact row -->
<section class="signature" style="top:322px">
  <div class="brand-backdrop"></div>
  <div class="brand-mark" style="left:40px;top:72px;width:76px;height:76px"></div>
  <div class="person-name" style="left:36px;top:26px">BARNABY CORMACK</div>
  <div class="person-role" style="left:36px;top:45px">Licensed Strata and Community Manager</div>
  <div class="brand-name" style="left:36px;top:156px;font-size:14.5px">CORMACK ESTATE GROUP</div>
  <div class="brand-tag" style="left:36px;top:174px;font-size:10.5px">STRATA MANAGEMENT SERVICES</div>
  <div class="contact" style="left:363px;top:157px">
    <svg style="color:var(--olive)"><use href="#icon-phone"/></svg>02.9376.5820<span class="gap"></span>
    <svg><use href="#icon-fax"/></svg>9463.7208
  </div>
  <div class="contact" style="left:363px;top:173px">
    <svg style="color:var(--olive)"><use href="#icon-web"/></svg>www.cormackestates.com.au
  </div>
  <div class="divider" style="left:543px;top:155px;height:34px"></div>
  <div class="company" style="left:556px;top:158px;font-size:10px">CORMACK ESTATE HOLDINGS PTY LTD</div>
  <div class="address" style="left:556px;top:172px;font-size:11px">164 Tallowood Street, ULTIMO NSW 2007</div>
  <p class="notice" style="left:36px;top:212px;width:640px">NOTICE: This e-mail message and accompanying data may contain information that is confidential and private If you are not the intended recipient, the use, dissemination, distribution or copying of this message or data is prohibited.</p>
  <p class="notice" style="left:36px;top:243px;width:640px">If you have received this e-mail in error please notify us immediately and delete all material pertaining to this e-mail. strata@cormackestates.com.au</p>
  <div class="social" style="left:700px;top:238px"><span></span><span></span><span></span><span></span></div>
</section>

<!-- Layout three: stacked contact columns -->
<section class="signature" style="top:594px">
  <div class="brand-backdrop"></div>
  <div class="brand-mark" style="left:40px;top:72px;width:76px;height:76px"></div>
  <div class="person-name" style="left:36px;top:26px">BARNABY CORMACK</div>
  <div class="person-role" style="left:36px;top:45px">Licensed Strata and Community Manager</div>
  <div class="brand-name" style="left:36px;top:156px;font-size:14.5px">CORMACK ESTATE GROUP</div>
  <div class="brand-tag" style="left:36px;top:174px;font-size:10.5px">STRATA MANAGEMENT SERVICES</div>
  <div class="contact" style="left:390px;top:142px">
    <svg style="color:var(--olive)"><use href="#icon-phone"/></svg>02.9376.5820
  </div>
  <div class="contact" style="left:390px;top:158px">
    <svg><use href="#icon-fax"/></svg>9463.7208
  </div>
  <div class="contact" style="left:390px;top:174px">
    <svg style="color:var(--olive)"><use href="#icon-web"/></svg>www.cormackestates.com.au
  </div>
  <div class="divider" style="left:560px;top:140px;height:50px"></div>
  <div class="company" style="left:572px;top:143px;font-size:10px">CORMACK ESTATE HOLDINGS PTY LTD</div>
  <div class="address" style="left:572px;top:157px;font-size:11px">164 Tallowood Street<br>ULTIMO NSW 2007</div>
  <p class="notice" style="left:36px;top:212px;width:640px">NOTICE: This e-mail message and accompanying data may contain information that is confidential and private If you are not the intended recipient, the use, dissemination, distribution or copying of this message or data is prohibited.</p>
  <p class="notice" style="left:36px;top:243px;width:640px">If you have received this e-mail in error please notify us immediately and delete all material pertaining to this e-mail. strata@cormackestates.com.au</p>
  <div class="social" style="left:700px;top:238px"><span></span><span></span><span></span><span></span></div>
</section>

</body>
</html>
```